Bramwell Exteriors Needs a New Website!

We are an exteriors company specializing in vinyl siding, Peter Aldous siding, aluminum soffit/fascia, trough. We do new construction work as well as renovations. We also build detached garages.
You can view our current website at www.bramwellbuilders.ca
I want to completely overhaul the website.
Our services are different now as we no longer do new home construction as well as we do not do the snow clearing.
I want to focus on 2 things in particular on the website:

1/ Exterior renovations

2/ Detached Garage construction.

I have included our logo in the attached files to use as well.

Some features we would like:

1/ Be able to easily attach a video from Youtube/Vimeo to highlight a product or service
2/ Quick chat or contact button that we can talk to a potential client quickly
3/ Meet the Team page that is interesting and fresh
4/ Place for us to put in helpful exterior tips/suggestions for homeowners.

Content is not important, but looking for the best design that will attract people once they click on our page and want to renovate with us.

Target Market(s)

People looking for renovations on their home, people looking to build a detached garage.

Industry/Entity Type

Residential Construction

Coding

Coded - Design and coding required

Number of Pages Required

5+ page

Font styles to use
Sans Serif

Requirements
Must have
• Fresh and exciting home page.

Simple design. Don't want it over complicated or too much information to confuse the potential client.

Easy way to contact us.

Meet the team page that instills confidence
Nice to have
• Colour of website to go off our logo. Doesn't need to be an exact match, but something that goes well with our blue and grey.

```html
<!DOCTYPE html>
<html lang="en">
<head>
<meta charset="utf-8">
<title>Bramwell Exteriors</title>
<link rel="stylesheet" href="https://fonts.googleapis.com/css2?family=Noto+Sans:wght@400;600;700&display=swap">
<style>
:root{
  --bg:#ffffff;
  --ink:#1f1f24;
  --muted:#6b6b72;
  --soft:#a7a7ae;
  --mauve:#a98ba9;
  --olive:#8e8f55;
  --panel:#fafafa;
}
*{box-sizing:border-box;margin:0;padding:0}
html,body{width:1200px;height:4852px;overflow:hidden;background:#f7f7f8}
body{font-family:"Noto Sans",sans-serif;color:var(--ink);position:relative}
.page{position:absolute;left:139px;top:193px;width:918px;height:4442px;background:var(--bg);overflow:hidden}
.abs{position:absolute}
.photo{position:absolute}
/* hero */
.hero{left:0;top:0;width:918px;height:428px;background:linear-gradient(180deg,#a9a7cf 0%,#d7b5c8 30%,#5d6478 55%,#8f8d8a 80%,#6d7069 100%)}
.brand{left:43px;top:22px;display:flex;align-items:center;gap:8px;color:#fff;font-weight:700;font-size:15px}
.brand i{width:26px;height:26px;border-radius:50%;background:#fff;display:block}
.nav{left:566px;top:30px;display:flex;gap:0;width:330px;justify-content:space-between;font-size:10px;color:#fff}
.hero-title{left:0;width:918px;top:168px;text-align:center;font-size:26px;color:#fff}
.hero-title span{color:var(--mauve)}
.hero-sub{left:0;width:918px;top:212px;text-align:center;font-size:10px;color:#fff}
.btn{left:408px;top:238px;width:102px;height:34px;background:var(--mauve);color:#fff;font-size:12px;display:flex;align-items:center;justify-content:center}
.dots{left:448px;top:401px;display:flex;gap:4px}
.dots i{width:5px;height:5px;border-radius:50%;background:#fff;opacity:.6}
.dots i:nth-child(2){opacity:1}
/* common */
.h2{font-size:14px;font-weight:600;line-height:20px;text-transform:uppercase}
.body{font-size:11px;line-height:17px;color:var(--muted);width:300px}
.more{font-size:9px;color:var(--olive);text-transform:uppercase}
/* experience box */
.exp-back{left:581px;top:499px;width:234px;height:259px;background:var(--mauve)}
.exp{left:603px;top:520px;width:231px;height:256px;background:#fff;border:2px solid #7e6a7e}
.exp .t{position:absolute;left:22px;top:28px;font-size:13px;line-height:20px;color:#444}
.exp .y{position:absolute;left:22px;top:88px;font-size:8px;line-height:14px;color:#444}
.exp .c{position:absolute;left:78px;top:145px;width:50px;height:50px;border-radius:50%;background:var(--mauve)}
.exp .n{position:absolute;left:35px;top:160px;font-size:46px;font-weight:700;color:#333}
/* service cards */
.svc{position:absolute;width:387px;height:490px}
.svc .img{position:absolute;left:0;top:0;width:368px;height:345px}
.svc .bar-r{position:absolute;left:293px;top:300px;width:11px;height:185px;background:var(--mauve)}
.svc .bar-b{position:absolute;left:8px;top:478px;width:296px;height:8px;background:var(--mauve)}
.svc .card{position:absolute;left:0;top:274px;width:293px;height:204px;background:#fff;padding:36px 38px}
.kicker{font-size:10px;color:var(--soft)}
.title{font-size:19px;color:#333;margin-top:4px}
.learn{font-size:9px;color:var(--mauve);text-transform:uppercase;margin-top:40px}
/* project */
.project{left:0;top:2456px;width:918px;height:623px;background:linear-gradient(180deg,#3f5a8c 0%,#8a86a9 35%,#c6a5a5 50%,#6b4a2f 70%,#2f3b20 100%)}
.proj-card{left:245px;top:3024px;width:428px;height:270px;background:var(--panel);padding:40px 34px}
.proj-card .body{width:320px;margin-top:22px}
.proj-card .learn{margin-top:36px}
/* blog */
.post{position:absolute;top:3533px;width:175px}
.post .img{height:155px}
.post .d{font-size:10px;color:var(--soft);margin:18px 0 0 16px}
.post .h{font-size:11px;line-height:17px;color:#333;margin:20px 0 0 16px;text-transform:uppercase}
.post .m{font-size:8px;color:var(--olive);margin:10px 0 0 16px;text-transform:uppercase}
/* footer */
.f-h{font-size:10px;color:#444}
.f-t{font-size:9px;line-height:15px;color:var(--soft)}
.f-links a{display:block;font-size:9px;color:var(--soft);text-decoration:none;line-height:25px}
.sub{left:598px;top:4101px;width:234px;height:36px;border:1px solid #ccc;display:flex}
.sub span{flex:1;font-size:9px;color:#777;padding:12px 8px}
.sub b{width:66px;background:var(--mauve);color:#fff;font-size:9px;font-weight:600;display:flex;align-items:center;justify-content:center}
.copy{left:0;width:918px;top:4318px;text-align:center;font-size:9px;color:var(--soft)}
</style>
</head>
<body>
<div class="page">
  <header>
    <div class="photo hero" role="img" aria-label="Two-storey house with grey siding and garages at dusk"></div>
    <div class="abs brand"><i></i>Bramwell Exteriors</div>
    <nav class="abs nav"><span>Home</span><span>Project</span><span>Services</span><span>About</span><span>Blog</span><span>Contact</span></nav>
    <h1 class="abs hero-title">Welcome to <span>BRAMWELL</span></h1>
    <p class="abs hero-sub">Lorem ipsum dolor sit amet consectetur adipisicing elit</p>
    <div class="abs btn">Get A Quote</div>
    <div class="abs dots"><i></i><i></i><i></i></div>
  </header>

  <section>
    <h2 class="abs h2" style="left:80px;top:522px;width:330px">We create building, and exterior design that enhance the human experience</h2>
    <p class="abs body" style="left:80px;top:580px">Lorem ipsum dolor sit amet, consectetur adipisicing elit. Ea, consequuntur, harum? Culpa iure vel fugiat veriatis obcaecati architecto.</p>
    <div class="abs more" style="left:80px;top:667px">More about us</div>
    <div class="abs exp-back"></div>
    <div class="abs exp">
      <div class="t">THE BEST IN EXTERIOR<br>DESIGN</div>
      <div class="y">YEARS OF<br>EXPERIENCE</div>
      <div class="c"></div>
      <div class="n">10</div>
    </div>
  </section>

  <section>
    <h2 class="abs h2" style="left:80px;top:941px">Our featured services</h2>
    <p class="abs body" style="left:80px;top:985px">Lorem ipsum dolor sit amet, consectetur adipisicing elit. Ea, consequuntur, harum? Culpa iure vel fugiat veriatis obcaecati architecto.</p>
    <div class="abs more" style="left:80px;top:1071px">More about us</div>

    <div class="svc" style="left:80px;top:1157px">
      <div class="photo img" style="background:linear-gradient(180deg,#4b5a86,#b59aa6 50%,#5a3b22 80%,#2f4a1f)" role="img" aria-label="Modern timber house at dusk"></div>
      <div class="bar-r"></div><div class="bar-b"></div>
      <div class="card"><div class="kicker">Exterior Design</div><div class="title">OBCAECATI ARCHITECTO</div><div class="learn">Learn more</div></div>
    </div>
    <div class="svc" style="left:467px;top:1157px">
      <div class="photo img" style="background:linear-gradient(180deg,#c9cfd6,#3c3f46 50%,#6e5a4c 75%,#d8dbdf)" role="img" aria-label="Dark sided home with snow on the roof"></div>
      <div class="bar-r"></div><div class="bar-b"></div>
      <div class="card"><div class="kicker">Exterior Design</div><div class="title">OBCAECATI ARCHITECTO</div><div class="learn">Learn more</div></div>
    </div>
    <div class="svc" style="left:80px;top:1693px">
      <div class="photo img" style="background:linear-gradient(180deg,#e6e6e6,#8c8580 45%,#b9b7b4 75%,#9a9591)" role="img" aria-label="Kitchen interior with grey cabinets"></div>
      <div class="bar-r"></div><div class="bar-b"></div>
      <div class="card"><div class="kicker">Exterior Design</div><div class="title">OBCAECATI ARCHITECTO</div><div class="learn">Learn more</div></div>
    </div>
    <div class="svc" style="left:467px;top:1693px">
      <div class="photo img" style="background:linear-gradient(180deg,#b4b4b2,#3b3b3d 50%,#7c6a58 75%,#5a4b3c)" role="img" aria-label="House under construction with stone front"></div>
      <div class="bar-r"></div><div class="bar-b"></div>
      <div class="card"><div class="kicker">Exterior Design</div><div class="title">OBCAECATI ARCHITECTO</div><div class="learn">Learn more</div></div>
    </div>
  </section>

  <section>
    <h2 class="abs h2" style="left:80px;top:2360px">Latest<br>projects</h2>
    <div class="abs more" style="right:82px;top:2373px;color:var(--mauve)">More about us</div>
    <div class="photo project" role="img" aria-label="Modern timber home with lawn at sunset"></div>
    <div class="abs dots" style="top:2963px"><i></i><i></i></div>
    <div class="abs proj-card">
      <div class="kicker">Exterior Design</div>
      <div class="title">OBCAECATI ARCHITECTO</div>
      <p class="body">Lorem ipsum dolor sit amet, consectetur adipisicing elit. Ea, consequuntur, harum? Culpa iure vel fugiat veriatis obcaecati architecto.</p>
      <div class="learn">View this project</div>
    </div>
  </section>

  <section>
    <h2 class="abs h2" style="left:80px;top:3394px">Blog and updates</h2>
    <p class="abs body" style="left:80px;top:3430px">Lorem ipsum dolor sit amet, consectetur adipisicing elit. Ea, consequuntur, harum? Culpa iure vel fugiat veriatis obcaecati architecto.</p>
    <article class="post" style="left:80px"><div class="photo img" style="position:relative;background:linear-gradient(180deg,#4b5a86,#b59aa6 50%,#5a3b22 80%,#2f4a1f)" role="img" aria-label="Modern timber house"></div><div class="d">July, 18 2020</div><div class="h">Iusto quos vienam<br>magni totam</div><div class="m">More about us</div></article>
    <article class="post" style="left:273px"><div class="photo img" style="position:relative;background:linear-gradient(180deg,#e6e6e6,#8c8580 45%,#b9b7b4)" role="img" aria-label="Kitchen interior"></div><div class="d">July, 18 2020</div><div class="h">Iusto quos vienam<br>magni totam</div><div class="m">More about us</div></article>
    <article class="post" style="left:467px"><div class="photo img" style="position:relative;background:linear-gradient(180deg,#c9cfd6,#3c3f46 50%,#d8dbdf)" role="img" aria-label="Dark sided home in snow"></div><div class="d">July, 18 2020</div><div class="h">Iusto quos vienam<br>magni totam</div><div class="m">More about us</div></article>
    <article class="post" style="left:661px"><div class="photo img" style="position:relative;background:linear-gradient(180deg,#b4b4b2,#3b3b3d 50%,#7c6a58)" role="img" aria-label="House under construction"></div><div class="d">July, 18 2020</div><div class="h">Iusto quos vienam<br>magni totam</div><div class="m">More about us</div></article>
  </section>

  <footer>
    <div class="abs" style="left:86px;top:4068px;width:200px">
      <div class="f-h">About Us</div>
      <p class="f-t" style="margin-top:22px">Lorem ipsum dolor sit amet, consectetur adipisicing elit. Ea, consequuntur, harum? Culpa iure vel fugiat veriatis obcaecati architecto.</p>
    </div>
    <div class="abs" style="left:341px;top:4068px">
      <div class="f-h">Features</div>
      <div class="f-links" style="margin-top:10px"><a>About Us</a><a>Testimonials</a><a>Terms of Service</a><a>Privacy</a><a>Contact Us</a></div>
    </div>
    <div class="abs f-h" style="left:598px;top:4068px">Subcribe to Newsletter</div>
    <div class="abs sub"><span>Enter Email</span><b>Subcribe</b></div>
    <div class="abs f-h" style="left:598px;top:4174px;font-size:9px">Follow Us</div>
    <div class="abs copy">Copyright @ 2020 All rights reserved</div>
  </footer>
</div>
</body>
</html>
```